Voltline Assemblies, Inc. Business Card

Voltline has three operating entities and I'm looking for a standard business card template that can be used for Voltline and the three operating entities that the logo just get swapped out, but has a very similar look and feel. Ultimately if someone had a business card from each, they assume the organizations are related because they all have the same look and feel.
Below are our websites and I will attached the logos for each entity:
https://www.voltlineassemblies.example/
https://www.brantoceramic.example/
https://www.omra-kfsd.example/
https://www.summitbreaker.example/

Target Market(s)

US Voltline

Industry/Entity Type

US Voltline

Contact Information for Business Card

Normal stuff

```html
<!DOCTYPE html>
<html lang="en">
<head>
<meta charset="utf-8">
<title>Voltline Assemblies, Inc. – Business Card Family</title>
<link href="https://fonts.googleapis.com/css2?family=Montserrat:wght@400;500;700&display=swap" rel="stylesheet">
<style>
  :root {
    --canvas: #e6e6e6;
    --paper: #ffffff;
    --voltline-red: #c8202f;
    --voltline-navy: #21306a;
    --branto-blue: #213f7a;
    --summit-slate: #4f7490;
    --omra-indigo: #06066b;
    --ink-light: #ffffff;
  }
  * { box-sizing: border-box; margin: 0; padding: 0; }
  html, body { width: 900px; height: 1200px; overflow: hidden; }
  body {
    background: var(--canvas);
    font-family: "Montserrat", Arial, sans-serif;
    position: relative;
  }
  .card {
    position: absolute;
    width: 323px;
    height: 209px;
    background: var(--paper);
    overflow: hidden;
  }
  .col-front { left: 115px; }
  .col-back { left: 462px; }
  .row-1 { top: 148px; }
  .row-2 { top: 379px; }
  .row-3 { top: 611px; }
  .row-4 { top: 842px; }

  .brand-voltline { --brand: var(--voltline-navy); --accent: var(--voltline-red); }
  .brand-branto   { --brand: var(--branto-blue);   --accent: var(--branto-blue); }
  .brand-summit   { --brand: var(--summit-slate);  --accent: var(--summit-slate); }
  .brand-omra     { --brand: var(--omra-indigo);   --accent: var(--omra-indigo); }

  .corner-block { position: absolute; top: 0; width: 14px; height: 30px; background: var(--brand); }
  .corner-left { left: 0; }
  .corner-right { right: 0; }
  .corner-red { background: var(--voltline-red); }

  /* Front */
  .front-mark {
    position: absolute;
    left: 0; right: 0; top: 52px;
    display: flex; flex-direction: column; align-items: center;
    color: var(--brand);
  }
  .mark-dot {
    width: 44px; height: 44px; border-radius: 50%;
    background: var(--brand);
    margin-bottom: 10px;
  }
  .front-name { font-weight: 700; font-size: 18px; line-height: 1; white-space: nowrap; }
  .front-tagline { font-size: 7px; font-weight: 500; margin-top: 5px; letter-spacing: 0.3px; }
  .web-band {
    position: absolute; left: 0; right: 0; bottom: 0; height: 29px;
    background: var(--accent);
    color: var(--ink-light);
    display: flex; align-items: center; justify-content: center; gap: 8px;
    font-size: 12.5px; font-weight: 400;
  }
  .web-band svg { width: 15px; height: 15px; }

  /* Back */
  .back-mark {
    position: absolute; left: 30px; right: 30px; top: 16px; height: 50px;
    display: flex; align-items: center; justify-content: center; gap: 8px;
    color: var(--brand);
  }
  .back-mark .mark-dot { width: 32px; height: 32px; margin: 0; flex: none; }
  .back-mark-text { display: flex; flex-direction: column; }
  .back-name { font-weight: 700; font-size: 13.5px; line-height: 1; white-space: nowrap; }
  .back-tagline { font-size: 6px; font-weight: 500; margin-top: 3px; white-space: nowrap; }
  .contact-band {
    position: absolute; left: 0; right: 0; top: 82px; height: 83px;
    background: var(--brand);
    color: var(--ink-light);
  }
  .person { position: absolute; left: 27px; top: 27px; }
  .person-name { font-weight: 700; font-size: 15.5px; line-height: 1; }
  .person-role { font-size: 8.5px; margin-top: 4px; }
  .divider {
    position: absolute; left: 162px; top: 14px; width: 1px; height: 56px;
    background: var(--ink-light);
  }
  .contact-list { position: absolute; left: 201px; top: 18px; list-style: none; }
  .contact-list li {
    display: flex; align-items: center; gap: 7px;
    font-size: 8px; height: 17px; letter-spacing: 0.2px;
  }
  .contact-list svg { width: 10px; height: 10px; }
</style>
</head>
<body>

<svg width="0" height="0" style="position:absolute">
  <defs>
    <symbol id="icon-globe" viewBox="0 0 16 16"><g fill="none" stroke="currentColor" stroke-width="1.1"><circle cx="8" cy="8" r="7"/><ellipse cx="8" cy="8" rx="3" ry="7"/><line x1="1" y1="8" x2="15" y2="8"/></g></symbol>
    <symbol id="icon-phone" viewBox="0 0 10 10"><rect x="2.5" y="0.6" width="5" height="8.8" rx="0.8" fill="none" stroke="currentColor" stroke-width="0.8"/><line x1="4.2" y1="8.1" x2="5.8" y2="8.1" stroke="currentColor" stroke-width="0.7"/></symbol>
    <symbol id="icon-mail" viewBox="0 0 10 10"><g fill="none" stroke="currentColor" stroke-width="0.8"><rect x="0.6" y="2" width="8.8" height="6.2" rx="0.5"/><polyline points="0.8,2.3 5,5.6 9.2,2.3"/></g></symbol>
    <symbol id="icon-pin" viewBox="0 0 10 10"><g fill="none" stroke="currentColor" stroke-width="0.8"><path d="M5 9.4 C2.4 6.6 1.6 5.2 1.6 3.9 A3.4 3.4 0 0 1 8.4 3.9 C8.4 5.2 7.6 6.6 5 9.4 Z"/><circle cx="5" cy="3.9" r="1.2"/></g></symbol>
  </defs>
</svg>

<!-- Voltline -->
<section class="card col-front row-1 brand-voltline">
  <div class="corner-block corner-left corner-red"></div>
  <div class="corner-block corner-right"></div>
  <div class="front-mark"><div class="mark-dot"></div><div class="front-name">VOLTLINE ASSEMBLIES, INC.</div></div>
  <div class="web-band"><svg><use href="#icon-globe"/></svg>https://www.voltlineassemblies.example/</div>
</section>
<section class="card col-back row-1 brand-voltline">
  <div class="corner-block corner-left"></div>
  <div class="corner-block corner-right corner-red"></div>
  <div class="back-mark"><div class="mark-dot"></div><div class="back-mark-text"><div class="back-name">VOLTLINE ASSEMBLIES, INC.</div></div></div>
  <div class="contact-band">
    <div class="person"><div class="person-name">YOUR NAME</div><div class="person-role">Your Position</div></div>
    <div class="divider"></div>
    <ul class="contact-list">
      <li><svg><use href="#icon-phone"/></svg>Your Number</li>
      <li><svg><use href="#icon-mail"/></svg>Your E-Mail</li>
      <li><svg><use href="#icon-pin"/></svg>Your Location</li>
    </ul>
  </div>
</section>

<!-- Branto -->
<section class="card col-front row-2 brand-branto">
  <div class="corner-block corner-left"></div>
  <div class="corner-block corner-right"></div>
  <div class="front-mark"><div class="mark-dot"></div><div class="front-name">BRANTO CERAMIC, LLC</div><div class="front-tagline">A Voltline Assemblies, Inc. Company</div></div>
  <div class="web-band"><svg><use href="#icon-globe"/></svg>https://www.brantoceramic.example/</div>
</section>
<section class="card col-back row-2 brand-branto">
  <div class="corner-block corner-left"></div>
  <div class="corner-block corner-right"></div>
  <div class="back-mark"><div class="mark-dot"></div><div class="back-mark-text"><div class="back-name">BRANTO CERAMIC, LLC</div><div class="back-tagline">A Voltline Assemblies, Inc. Company</div></div></div>
  <div class="contact-band">
    <div class="person"><div class="person-name">YOUR NAME</div><div class="person-role">Your Position</div></div>
    <div class="divider"></div>
    <ul class="contact-list">
      <li><svg><use href="#icon-phone"/></svg>Your Number</li>
      <li><svg><use href="#icon-mail"/></svg>Your E-Mail</li>
      <li><svg><use href="#icon-pin"/></svg>Your Location</li>
    </ul>
  </div>
</section>

<!-- Summit -->
<section class="card col-front row-3 brand-summit">
  <div class="corner-block corner-left"></div>
  <div class="corner-block corner-right"></div>
  <div class="front-mark"><div class="mark-dot"></div><div class="front-name">SUMMIT BREAKER</div><div class="front-tagline">A Voltline Assemblies, Inc. Company</div></div>
  <div class="web-band"><svg><use href="#icon-globe"/></svg>https://www.summitbreaker.example/</div>
</section>
<section class="card col-back row-3 brand-summit">
  <div class="corner-block corner-left"></div>
  <div class="corner-block corner-right"></div>
  <div class="back-mark"><div class="mark-dot"></div><div class="back-mark-text"><div class="back-name">SUMMIT BREAKER</div><div class="back-tagline">A Voltline Assemblies, Inc. Company</div></div></div>
  <div class="contact-band">
    <div class="person"><div class="person-name">YOUR NAME</div><div class="person-role">Your Position</div></div>
    <div class="divider"></div>
    <ul class="contact-list">
      <li><svg><use href="#icon-phone"/></svg>Your Number</li>
      <li><svg><use href="#icon-mail"/></svg>Your E-Mail</li>
      <li><svg><use href="#icon-pin"/></svg>Your Location</li>
    </ul>
  </div>
</section>

<!-- Omra -->
<section class="card col-front row-4 brand-omra">
  <div class="corner-block corner-left"></div>
  <div class="corner-block corner-right"></div>
  <div class="front-mark"><div class="mark-dot"></div><div class="front-name">OMRA TRANSFORMER CORP.</div><div class="front-tagline">A Voltline Assemblies, Inc. Company</div></div>
  <div class="web-band"><svg><use href="#icon-globe"/></svg>https://www.omra-kfsd.example/</div>
</section>
<section class="card col-back row-4 brand-omra">
  <div class="corner-block corner-left"></div>
  <div class="corner-block corner-right"></div>
  <div class="back-mark"><div class="mark-dot"></div><div class="back-mark-text"><div class="back-name">OMRA TRANSFORMER CORP.</div><div class="back-tagline">A Voltline Assemblies, Inc. Company</div></div></div>
  <div class="contact-band">
    <div class="person"><div class="person-name">YOUR NAME</div><div class="person-role">Your Position</div></div>
    <div class="divider"></div>
    <ul class="contact-list">
      <li><svg><use href="#icon-phone"/></svg>Your Number</li>
      <li><svg><use href="#icon-mail"/></svg>Your E-Mail</li>
      <li><svg><use href="#icon-pin"/></svg>Your Location</li>
    </ul>
  </div>
</section>

</body>
</html>
```